Quarvine, Cosmetic skin care line

I am not looking to change my logo quarvine on the label just want someone to design a different label I want it to be very classy as it is already just want something different. My product target classier people and people with higher income and for woman and men but mostly women. Looking to keep the label background black

Target Market(s)

Classier and higer income women/men mostly women

Industry/Entity Type

Cosmetics

• I don't really know

Colors

Designer to choose colors to be used in the design.

Requirements
Must have
• It must keep the same quarvine logo and the same matte black background color
Nice to have
• I want a different layout and maybe different fonts for the label
Should not have

```html
<!DOCTYPE html>
<html lang="en">
<head>
<meta charset="utf-8">
<title>Quarvine — Eye Corrector Labels</title>
<link href="https://fonts.googleapis.com/css2?family=Oswald:wght@300;500&display=swap" rel="stylesheet">
<style>
  :root {
    --canvas: #ffffff;
    --label-black: #0b0b0c;
    --label-ink: #ffffff;
    --rule: #e6e6e6;
  }
  * { box-sizing: border-box; margin: 0; padding: 0; }
  html, body {
    width: 1200px;
    height: 994px;
    overflow: hidden;
    background: var(--canvas);
  }
  .canvas {
    position: relative;
    width: 1200px;
    height: 994px;
    background: var(--canvas);
    font-family: "Oswald", sans-serif;
    color: var(--label-ink);
  }
  .label {
    position: absolute;
    background: var(--label-black);
  }
  .label__rule {
    position: absolute;
    left: 0;
    height: 0;
    border-top: 1px solid var(--rule);
  }
  .brand {
    position: absolute;
    font-weight: 300;
    text-transform: uppercase;
    line-height: 1;
  }
  .brand__name { display: block; letter-spacing: 0.32em; }
  .brand__tagline { display: block; letter-spacing: 0.14em; }
  .product {
    position: absolute;
    text-align: right;
    font-weight: 500;
    text-transform: uppercase;
    line-height: 1;
  }
  .product__range, .product__detail { display: block; }
  .product__name { display: block; }

  /* Serum label — portrait */
  .label--serum { left: 698px; top: 91px; width: 332px; height: 492px; }
  .label--serum .label__rule--top { top: 47px; width: 330px; }
  .label--serum .label__rule--bottom { top: 443px; width: 330px; }
  .label--serum .brand { left: 25px; top: 100px; }
  .label--serum .brand__name { font-size: 46px; }
  .label--serum .brand__tagline { font-size: 20px; margin-top: 22px; }
  .label--serum .product { right: 23px; top: 297px; }
  .label--serum .product__range { font-size: 20px; }
  .label--serum .product__name { font-size: 42px; margin-top: 8px; }
  .label--serum .product__detail { font-size: 21px; margin-top: 6px; line-height: 1.35; }

  /* Gel label — landscape */
  .label--gel { left: 619px; top: 622px; width: 479px; height: 252px; }
  .label--gel .label__rule--top { top: 30px; left: 2px; width: 474px; }
  .label--gel .label__rule--bottom { top: 223px; left: 2px; width: 474px; }
  .label--gel .brand { left: 19px; top: 62px; }
  .label--gel .brand__name { font-size: 40px; }
  .label--gel .brand__tagline { font-size: 17px; margin-top: 13px; }
  .label--gel .product { right: 25px; top: 108px; }
  .label--gel .product__range { font-size: 17px; }
  .label--gel .product__name { font-size: 31px; margin-top: 5px; }
  .label--gel .product__detail { font-size: 17px; margin-top: 6px; line-height: 1.35; }
</style>
</head>
<body>
<main class="canvas">

  <section class="label label--serum" aria-label="Eye corrector serum label">
    <div class="label__rule label__rule--top"></div>
    <div class="brand">
      <span class="brand__name">Quarvine</span>
      <span class="brand__tagline">For all</span>
    </div>
    <div class="product">
      <span class="product__range">Eye corrector</span>
      <span class="product__name">Serum</span>
      <span class="product__detail">With triple<br>peptides</span>
    </div>
    <div class="label__rule label__rule--bottom"></div>
  </section>

  <section class="label label--gel" aria-label="Herbal eye gel label">
    <div class="label__rule label__rule--top"></div>
    <div class="brand">
      <span class="brand__name">Quarvine</span>
      <span class="brand__tagline">For all</span>
    </div>
    <div class="product">
      <span class="product__range">Eye corrector</span>
      <span class="product__name">Herbal eye gel</span>
      <span class="product__detail">With triple<br>peptides</span>
    </div>
    <div class="label__rule label__rule--bottom"></div>
  </section>

</main>
</body>
</html>
```